Marova Hand Wash

Design hand washes. Total 12 variants to be designed.

Variants name are:

1) MILK &OLIVE
2) Shea Butter
3) Hidden Glow
4) Cream and Peach
5) Milk and Honey
6) Amber Riddle
7) Bakhour
8) Musk
9) White Oud
10) Black Oud
11) Rose Oud
12) Oud & Sandalwood

Labels can be on transparent sticker or background colors. All variants will be differentiated by fragrances and color. Bottle will be transparent. Pumps used for dispensing will be in Black or Transparent Color.

Designers can initially present designs of 4-5 variants initially. Later based on feedback, they can work out on more.

Bottle is 400ml and shape is rectangle. Ignore the size on bottle picture. Bottle keyline is attached.

Target Market(s)

B+, B, C+

Requirements
Must have
• Some relation to the variant names

```html
<!DOCTYPE html>
<html lang="en">
<head>
<meta charset="utf-8">
<title>Marova Hand Wash – Range</title>
<link href="https://fonts.googleapis.com/css2?family=Signika:wght@300;400;600&family=Kaushan+Script&display=swap" rel="stylesheet">
<style>
  :root{
    --canvas:#ffffff;
    --code-grey:#c4c4c4;
    --brand-violet:#4a3f94;
    --pump-light:#f4f4f4;
    --pump-mid:#d6d6d6;
    --pump-dark:#bdbdbd;
    --olive-body:#c9d87a;
    --olive-edge:#b4c85a;
    --olive-ink:#2f6b1f;
    --olive-tag:#2c5a1c;
    --peach-body:#fdbd68;
    --peach-edge:#f7a640;
    --peach-ink:#c35a2a;
    --peach-tag:#c4542b;
    --amber-body:#f4ecdf;
    --amber-edge:#e6dac6;
    --amber-ink:#8a6442;
    --amber-tag:#a97d57;
    --rose-body:#dc8aa3;
    --rose-edge:#cc6e8c;
    --rose-ink:#b0185a;
    --rose-tag:#b0185a;
  }
  *{box-sizing:border-box;margin:0;padding:0}
  html,body{width:1200px;height:701px;overflow:hidden;background:var(--canvas)}
  .range{position:relative;width:1200px;height:701px;font-family:"Signika",sans-serif}
  .range-code{position:absolute;left:20px;top:30px;font-weight:300;font-size:36px;color:var(--code-grey);letter-spacing:1px}

  .bottle{position:absolute;top:98px;width:210px;height:500px}
  .pump-spout{position:absolute;left:46px;top:2px;width:166px;height:18px;background:linear-gradient(180deg,var(--pump-light),var(--pump-dark));border-radius:4px 10px 3px 3px;transform:skewY(-2deg)}
  .pump-stem{position:absolute;left:86px;top:18px;width:36px;height:14px;background:linear-gradient(90deg,var(--pump-mid),var(--pump-light),var(--pump-mid))}
  .pump-neck{position:absolute;left:68px;top:32px;width:72px;height:24px;background:linear-gradient(90deg,var(--pump-mid),var(--pump-light),var(--pump-mid))}
  .pump-cap{position:absolute;left:50px;top:54px;width:108px;height:86px;background:linear-gradient(90deg,var(--pump-dark),var(--pump-light) 45%,var(--pump-mid));border-radius:3px}
  .body{position:absolute;left:0;top:138px;width:210px;height:360px;border-radius:26px;background:linear-gradient(90deg,var(--edge),var(--fill) 20%,var(--fill) 80%,var(--edge))}
  .shadow{position:absolute;left:0;top:498px;width:210px;height:40px;background:linear-gradient(180deg,rgba(0,0,0,.06),rgba(0,0,0,0));border-radius:0 0 20px 20px}

  .label{position:absolute;left:26px;top:160px;width:156px;height:302px;border-radius:12px;overflow:hidden;background:linear-gradient(180deg,#fff 0%,#fff 38%,var(--glow) 100%);text-align:center}
  .brand{position:absolute;left:0;right:0;top:40px;display:flex;justify-content:center;align-items:center;gap:6px;font-weight:600;font-size:30px;color:var(--brand-violet)}
  .brand-dot{width:8px;height:8px;border-radius:50%;background:var(--brand-violet)}
  .variant-lead{position:absolute;left:0;right:0;top:108px;font-size:19px;color:var(--ink)}
  .variant-name{position:absolute;left:0;right:0;top:124px;font-family:"Kaushan Script",cursive;font-size:38px;color:var(--ink)}
  .artwork{position:absolute;left:22px;top:190px;width:112px;height:54px;border-radius:28px}
  .tag{position:absolute;left:50px;top:242px;width:56px;height:60px;background:var(--tag);color:#fff}
  .tag-type{display:block;margin-top:6px;font-size:10px;line-height:11px;letter-spacing:2.5px}
  .tag-rule{display:block;width:42px;height:1px;background:rgba(255,255,255,.7);margin:5px auto 3px}
  .tag-size{display:block;font-size:8px;font-weight:300}

  .olive{left:116px;--fill:var(--olive-body);--edge:var(--olive-edge);--ink:var(--olive-ink);--tag:var(--olive-tag);--glow:#a9cc52}
  .peach{left:369px;--fill:var(--peach-body);--edge:var(--peach-edge);--ink:var(--peach-ink);--tag:var(--peach-tag);--glow:#fbb35b}
  .amber{left:621px;--fill:var(--amber-body);--edge:var(--amber-edge);--ink:var(--amber-ink);--tag:var(--amber-tag);--glow:#dcb88f}
  .rose{left:874px;--fill:var(--rose-body);--edge:var(--rose-edge);--ink:var(--rose-ink);--tag:var(--rose-tag);--glow:#f2b6c8}

  .olive .artwork{background:radial-gradient(circle,#a6c935,#4f7d27 75%)}
  .peach .artwork{background:radial-gradient(circle,#f6a038,#d9611f 75%)}
  .amber .artwork{background:radial-gradient(circle,#f6efd8,#6b4630 80%)}
  .rose .artwork{background:radial-gradient(circle,#f3bcc8,#3d6b3a 85%)}
</style>
</head>
<body>
<main class="range">
  <div class="range-code">BG-2</div>

  <section class="bottle olive">
    <div class="pump-spout"></div><div class="pump-stem"></div><div class="pump-neck"></div><div class="pump-cap"></div>
    <div class="body"></div><div class="shadow"></div>
    <div class="label">
      <div class="brand"><span>Marova</span><span class="brand-dot"></span></div>
      <div class="variant-lead">Milk and</div>
      <div class="variant-name">Olive</div>
      <div class="artwork" role="img" aria-label="Illustration of green olives with leaves"></div>
      <div class="tag"><span class="tag-type">HAND WASH</span><span class="tag-rule"></span><span class="tag-size">- 400 mL -</span></div>
    </div>
  </section>

  <section class="bottle peach">
    <div class="pump-spout"></div><div class="pump-stem"></div><div class="pump-neck"></div><div class="pump-cap"></div>
    <div class="body"></div><div class="shadow"></div>
    <div class="label">
      <div class="brand"><span>Marova</span><span class="brand-dot"></span></div>
      <div class="variant-lead">Cream and</div>
      <div class="variant-name">Peach</div>
      <div class="artwork" role="img" aria-label="Illustration of two ripe peaches with a leaf"></div>
      <div class="tag"><span class="tag-type">HAND WASH</span><span class="tag-rule"></span><span class="tag-size">- 400 mL -</span></div>
    </div>
  </section>

  <section class="bottle amber">
    <div class="pump-spout"></div><div class="pump-stem"></div><div class="pump-neck"></div><div class="pump-cap"></div>
    <div class="body"></div><div class="shadow"></div>
    <div class="label">
      <div class="brand"><span>Marova</span><span class="brand-dot"></span></div>
      <div class="variant-lead">Amber</div>
      <div class="variant-name">Riddle</div>
      <div class="artwork" role="img" aria-label="Illustration of vanilla pods with white blossoms"></div>
      <div class="tag"><span class="tag-type">HAND WASH</span><span class="tag-rule"></span><span class="tag-size">- 400 mL -</span></div>
    </div>
  </section>

  <section class="bottle rose">
    <div class="pump-spout"></div><div class="pump-stem"></div><div class="pump-neck"></div><div class="pump-cap"></div>
    <div class="body"></div><div class="shadow"></div>
    <div class="label">
      <div class="brand"><span>Marova</span><span class="brand-dot"></span></div>
      <div class="variant-lead">Rose</div>
      <div class="variant-name">Oud</div>
      <div class="artwork" role="img" aria-label="Illustration of a pink rose with green leaves"></div>
      <div class="tag"><span class="tag-type">HAND WASH</span><span class="tag-rule"></span><span class="tag-size">- 400 mL -</span></div>
    </div>
  </section>
</main>
</body>
</html>
```